Are you a woman over 50 who can’t lose weight?

Ads attracting 50 and older women/men who are looking for holistic metabolism improving solutions and can’t lose weight on their own.(please see my website: gobrivanhealth.com) Descriptions saying this is a program designed to improve your metabolism NOT another fad diet. Every plan is customized to each patients needs (no cookie cutter plans) and overseen by a healthcare provider. Will be taught which foods are best for their individual body with special technology. No exercise needed to lose weight or inches. Dr. Neil Sorrow, DC who will oversee your care was listed as the 2018 Wellness Champion for all of Central Louisiana. Our patients lose up to one pound of fat per day AND are supported on keeping it off. We do Body Composition analyses, 3-D body scans, Biocommunication, and Body Fat elimination technologies to help you succeed. We have been serving Mivo for 12 years and have great reviews online. We are an A+ business with the Fair Trade Registry. We are locally owned and not affiliated with any franchises.

Target Market(s)

Women 50-70years old

Industry/Entity Type

Health And Wellness

Font styles to use
Serif

Colors

Designer to choose colors to be used in the design.

Requirements
Must have
• Brivan logo, website to see testimonials, 3-D Body scan for first time visitor for $20 ($150 value). Scan will show measurements, body fat percentage, and lots of other metabolic information.
Nice to have
• Look at my website: gobrivanhealth.com for my logo please and other information

```html
<!DOCTYPE html>
<html lang="en">
<head>
<meta charset="utf-8">
<title>Brivan – Improve Your Metabolism</title>
<link href="https://fonts.googleapis.com/css2?family=Bebas+Neue&family=Montserrat:wght@400;600;700&display=swap" rel="stylesheet">
<style>
  :root {
    --green: #8cc63f;
    --charcoal: #444547;
    --white: #ffffff;
    --stage: #e9ebe7;
    --photo-light: #eef3f6;
    --photo-mid: #c9d6de;
  }
  * { margin: 0; padding: 0; box-sizing: border-box; }
  html, body { width: 1200px; height: 750px; overflow: hidden; }
  body {
    background: var(--stage);
    font-family: "Montserrat", sans-serif;
    color: var(--charcoal);
    position: relative;
  }
  .ad {
    position: absolute;
    left: 374px; top: 0;
    width: 452px; height: 750px;
    background: var(--white);
    overflow: hidden;
  }
  .corner-accent { position: absolute; left: 0; top: 0; }
  .hero-photo {
    position: absolute;
    left: 187px; top: 104px;
    width: 265px; height: 410px;
    background: radial-gradient(ellipse at 55% 45%, var(--photo-light) 0%, var(--photo-mid) 70%, var(--white) 100%);
  }
  .headline {
    position: absolute;
    left: 32px; top: 22px;
    font-family: "Bebas Neue", sans-serif;
    font-size: 76px;
    line-height: 0.88;
    font-weight: 400;
    letter-spacing: -0.5px;
    color: var(--charcoal);
    text-transform: uppercase;
  }
  .tagline-bar {
    position: absolute;
    left: 21px; top: 160px;
    width: 310px; height: 36px;
    background: var(--charcoal);
    border-radius: 18px 0 0 18px;
    color: var(--green);
    font-size: 19px;
    font-weight: 600;
    line-height: 36px;
    padding-left: 20px;
  }
  .intro {
    position: absolute;
    left: 33px; top: 205px;
    width: 228px;
    font-size: 10.6px;
    line-height: 1.24;
  }
  .doctor-name {
    position: absolute;
    left: 33px; top: 308px;
    font-family: "Bebas Neue", sans-serif;
    font-size: 26px;
    color: var(--green);
    line-height: 1;
  }
  .doctor-bio {
    position: absolute;
    left: 33px; top: 333px;
    width: 140px;
    font-size: 10.6px;
    line-height: 1.3;
  }
  .doctor-bio strong { font-weight: 700; }
  .scan-badge { position: absolute; left: 100px; top: 376px; z-index: 3; }
  .scan-band {
    position: absolute;
    z-index: 2;
    left: 30px; top: 502px;
    width: 392px; height: 46px;
    background: var(--green);
    border-radius: 23px;
    font-size: 11.5px;
    font-weight: 700;
    line-height: 1.25;
    text-align: center;
    display: flex; align-items: center; justify-content: center;
  }
  .about {
    position: absolute;
    z-index: 1;
    left: 0; top: 534px;
    width: 277px; height: 164px;
    background: var(--charcoal);
    color: var(--white);
    font-size: 10.4px;
    line-height: 1.26;
    padding: 23px 20px 0 32px;
  }
  .brand {
    position: absolute;
    left: 285px; top: 565px;
    display: flex; align-items: center; gap: 6px;
  }
  .brand-name {
    font-size: 28px;
    font-weight: 700;
    color: var(--charcoal);
    letter-spacing: -0.5px;
  }
  .brand-dot {
    width: 10px; height: 10px;
    border-radius: 50%;
    background: var(--green);
  }
  .address {
    position: absolute;
    left: 285px; top: 616px;
    font-size: 9.6px;
    line-height: 1.3;
  }
  .phone-bar {
    position: absolute;
    left: 277px; top: 648px;
    width: 175px; height: 42px;
    background: var(--green);
    font-family: "Bebas Neue", sans-serif;
    font-size: 32px;
    line-height: 44px;
    padding-left: 8px;
    color: var(--charcoal);
  }
  .web-band {
    position: absolute;
    left: 0; top: 698px;
    width: 452px; height: 52px;
    background: var(--green);
    font-size: 15.5px;
    font-weight: 600;
    text-align: center;
    line-height: 54px;
  }
</style>
</head>
<body>
  <div class="ad">
    <svg class="corner-accent" width="298" height="212" viewBox="0 0 298 212">
      <polygon points="0,0 298,0 0,212" fill="#8cc63f"/>
    </svg>
    <div class="hero-photo" role="img" aria-label="Smiling senior couple in white shirts embracing outdoors"></div>

    <h1 class="headline">Improve Your<br>Metabolism</h1>
    <div class="tagline-bar">NOT another fad diet.</div>

    <p class="intro">Every plan is customized to each patients needs (no cookie cutter plans) and overseen by a healthcare provider. Will be taught which foods are best for their individual body with special technology. No exercise needed to lose weight or inches.</p>

    <h2 class="doctor-name">Dr. Neil Sorrow</h2>
    <p class="doctor-bio">DC who will oversee your care was listed as the <strong>2018</strong> Wellness Champion for all of <strong>Central Louisiana.</strong></p>

    <svg class="scan-badge" width="130" height="130" viewBox="0 0 130 130">
      <circle cx="64" cy="64" r="55" fill="#ffffff" stroke="#444547" stroke-width="2.5"/>
      <g transform="rotate(14 64 64)" fill="#444547" text-anchor="middle">
        <text x="66" y="36" font-family="Bebas Neue, sans-serif" font-size="19">3-D Body</text>
        <text x="64" y="68" font-family="Bebas Neue, sans-serif" font-size="36">Scan</text>
        <text x="64" y="84" font-family="Montserrat, sans-serif" font-size="10.5">for first time</text>
        <text x="62" y="96" font-family="Montserrat, sans-serif" font-size="10.5">visitor for</text>
        <rect x="12" y="100" width="96" height="20" rx="10" fill="#444547"/>
        <text x="60" y="115" fill="#ffffff" font-family="Montserrat, sans-serif" font-weight="700" font-size="12">$20 <tspan font-size="8.5">($150 value)</tspan></text>
      </g>
    </svg>

    <div class="scan-band"><span>Scan will show measurements, body fat percentage,<br>and lots of other metabolic information.</span></div>

    <p class="about">Our patients lose up to one pound of fat per day AND are supported on keeping it off. We do Body Composition analyses, 3-D body scans, Biocommunication, and Body Fat elimination technologies to help you succeed. We have been serving Mivo for 12 years and have great reviews online. We are an A+ business with the Fair Trade Registry. We are locally owned and not affiliated with any franchises.</p>

    <div class="brand">
      <span class="brand-name">Brivan</span>
      <span class="brand-dot"></span>
    </div>
    <p class="address">1840 Magnolia Rd<br>Alder, LA 71299</p>
    <div class="phone-bar">318-555-0147</div>

    <div class="web-band">www.gobrivanhealth.com</div>
  </div>
</body>
</html>
```